Stationery Design Project - Dunmore-Kestrel

Letterhead
Size: A4 - 210mm x 297mm

With Compliments Slip
Size: DL - 210mm x 99mm

Notepad
Size: 250mm x 140mm

Presentation Folder
Size: A4

-
Dunmore-Kestrel Executive Search & Consulting
*Perth *Brisbane *Seoul *Hongkong

Website to be: www.dunmorekestrel.com.au

Head Hunting & Recruitment Agency

Area we recruit in:
Executive & General Management
Government & Public Sector
Executive Contracting
Accounting
Banking & Financial Services
Information Technology & Telecommunications
Legal
Operations, Engineering & Construction
Human Resources
Board Appointments

Please note we love the business card design so if we can keep that design inline that would be great.

Best of luck

Neville

```html
<!DOCTYPE html>
<html lang="en">
<head>
<meta charset="utf-8">
<title>Dunmore-Kestrel Notepad</title>
<link href="https://fonts.googleapis.com/css2?family=Cinzel:wght@400&family=Open+Sans:wght@400&display=swap" rel="stylesheet">
<style>
  :root {
    --backdrop: #ececec;
    --silver-edge: #d6d7d9;
    --silver-light: #f6f6f6;
    --ink: #3a3c42;
    --ink-soft: #5a5d63;
    --mark: #8a8d93;
    --band: #1b1b1b;
    --band-text: #ffffff;
    --slate-light: #cfd1d5;
    --slate-mid: #a4a7ad;
    --slate-dark: #6a6e75;
    --paper: #ffffff;
    --rule: #a9abae;
    --punch: #dcdcdc;
  }
  * { margin: 0; padding: 0; box-sizing: border-box; }
  html, body { width: 1200px; height: 846px; overflow: hidden; }
  body { background: var(--backdrop); position: relative; }

  .cover {
    position: absolute; left: 109px; top: 74px; width: 493px; height: 698px;
    background: linear-gradient(90deg, var(--silver-edge) 0%, var(--silver-light) 45%, var(--silver-edge) 100%);
    overflow: hidden;
  }
  .cover__mark {
    position: absolute; top: 140px; left: 212px; width: 70px; height: 70px;
    background: var(--mark);
  }
  .cover__name {
    position: absolute; top: 252px; left: 0; width: 100%; text-align: center;
    font-family: "Cinzel", serif; font-size: 29px; color: var(--ink); letter-spacing: 0.5px;
  }
  .cover__tagline {
    position: absolute; top: 290px; left: 0; width: 100%; text-align: center;
    font-family: "Cinzel", serif; font-size: 14px; color: var(--ink-soft); letter-spacing: 1.6px;
  }
  .cover__band {
    position: absolute; top: 384px; left: 0; width: 100%; height: 22px;
    background: var(--band); color: var(--band-text);
    font-family: "Open Sans", sans-serif; font-size: 11px;
    display: flex; align-items: center; justify-content: center; padding-left: 30px;
  }
  .cover__artwork {
    position: absolute; top: 413px; left: 0; width: 100%; height: 285px;
    background: radial-gradient(ellipse 70% 80% at 62% 40%, var(--slate-light) 0%, var(--slate-mid) 50%, var(--slate-dark) 100%);
  }

  .notepage {
    position: absolute; left: 626px; top: 74px; width: 495px; height: 698px;
    background: var(--paper);
  }
  .notepage__punches {
    position: absolute; left: 18px; top: 27px; width: 12px; height: 660px;
    background: repeating-linear-gradient(to bottom, var(--punch) 0 11px, transparent 11px 27.7px);
  }
  .notepage__mark {
    position: absolute; left: 105px; top: 64px; width: 30px; height: 30px;
    background: var(--mark);
  }
  .notepage__name {
    position: absolute; left: 57px; top: 110px;
    font-family: "Cinzel", serif; font-size: 13.5px; color: var(--ink);
  }
  .notepage__tagline {
    position: absolute; left: 68px; top: 127px;
    font-family: "Cinzel", serif; font-size: 5.5px; color: var(--ink-soft); letter-spacing: 0.5px;
  }
  .notepage__rules {
    position: absolute; left: 57px; top: 79px; width: 404px;
    display: flex; flex-direction: column; align-items: flex-end; gap: 31.3px;
  }
  .notepage__rule { width: 100%; border-top: 1px dashed var(--rule); }
  .notepage__rule--short { width: 254px; }
</style>
</head>
<body>
  <section class="cover">
    <div class="cover__mark" role="img" aria-label="Company mark"></div>
    <div class="cover__name">Dunmore Kestrel</div>
    <div class="cover__tagline">EXECUTIVE SEARCH &amp; CONSULTING</div>
    <div class="cover__band">www.dunmorekestrel.com.au</div>
    <div class="cover__artwork" role="img" aria-label="Large faint embossed jigsaw pieces in slate grey with a soft light sheen"></div>
  </section>

  <section class="notepage">
    <div class="notepage__punches"></div>
    <div class="notepage__mark" role="img" aria-label="Company mark"></div>
    <div class="notepage__name">Dunmore Kestrel</div>
    <div class="notepage__tagline">EXECUTIVE SEARCH &amp; CONSULTING</div>
    <div class="notepage__rules">
      <div class="notepage__rule notepage__rule--short"></div>
      <div class="notepage__rule notepage__rule--short"></div>
      <div class="notepage__rule"></div>
      <div class="notepage__rule"></div>
      <div class="notepage__rule"></div>
      <div class="notepage__rule"></div>
      <div class="notepage__rule"></div>
      <div class="notepage__rule"></div>
      <div class="notepage__rule"></div>
      <div class="notepage__rule"></div>
      <div class="notepage__rule"></div>
      <div class="notepage__rule"></div>
      <div class="notepage__rule"></div>
      <div class="notepage__rule"></div>
      <div class="notepage__rule"></div>
      <div class="notepage__rule"></div>
      <div class="notepage__rule"></div>
      <div class="notepage__rule"></div>
    </div>
  </section>
</body>
</html>
```